Online Cooking App Pitch Deck- (THIS IS NOT A FOOD BUSINESS OR FOOD SERVICE, NO FOOD PICTURES)

Project Goal:
Design a visually compelling pitch deck to be used for securing investment. Looking for the pitch deck to be about the design using shapes, colors, fonts and sizes. Must be creative yet simple and clean.
Color Palette:
https://huebrik.io/ff3800-ffe2db-fefefa-2d3e50-010b13

(We want most screens to use #FEFEFA)

This is the current pitch deck we need simplified and redesigned (USE TEXT IN THE VANDREL LINK TO SHOW IN YOUR DESIGN):

https://files.vandrel.net/slides/d/7QpLmZ2kTr84NwXaVbcY0-hoxjdEuvwKt/view?mode=share&uid=503921846170259384712&fmt=true&sd=true

Project is now guaranteed. Remember use the text in the vandrel link in powerpoint design. Use a little more color not just the logo color. Do not use any pictures of food this is not food related business. We care more about style and design of shapes, text, color fonts.

Target Market(s)

Investors (venture capitalists, angel investors) interested in innovative technology solutions within the food industry.

Font styles to use
Serif
Sans Serif

Requirements
Nice to have
• Simple, abstract background non distracting but complementary.
Should not have
• No pictures

```html
<!DOCTYPE html>
<html lang="en">
<head>
<meta charset="utf-8">
<title>Ladle &amp; Line — Pitch Deck Overview</title>
<link href="https://fonts.googleapis.com/css2?family=Poppins:wght@400;500;600;700;800&display=swap" rel="stylesheet">
<style>
  :root{
    --orange:#ff3800;
    --blush:#ffe2db;
    --paper:#fefefa;
    --slate:#2d3e50;
    --ink:#010b13;
    --stage:#e9e7ea;
    --night:#1b1c21;
    --body:#4a4f57;
  }
  *{box-sizing:border-box;margin:0;padding:0}
  html,body{width:1046px;height:1200px;overflow:hidden}
  body{background:var(--stage);font-family:"Poppins",sans-serif;color:var(--ink);position:relative}
  .slide{position:absolute;width:460px;height:259px;overflow:hidden;background:var(--paper)}
  .col-a{left:44px}.col-b{left:542px}
  .row-1{top:34px}.row-2{top:325px}.row-3{top:616px}.row-4{top:907px}
  .abs{position:absolute}
  .shape{position:absolute;overflow:hidden}
  .shape svg{display:block;width:100%;height:100%}

  /* cover */
  .cover{background:var(--night)}
  .cover .backdrop{left:230px;top:0;width:230px;height:259px;background:linear-gradient(160deg,#23262d,#121418)}
  .cover .drop{left:0;top:0;width:260px;height:259px;background:var(--orange);border-radius:50% 0 50% 50%}
  .cover .drop-inner{left:22px;top:22px;width:217px;height:214px;border-radius:50% 0 50% 50%;background:linear-gradient(165deg,var(--slate) 0%,#1a2633 100%)}
  .cover .date{left:372px;top:39px;width:64px;height:22px;border-radius:11px;background:var(--orange);color:#fff;font-size:7.5px;font-weight:700;display:flex;align-items:center;justify-content:center}
  .cover .brand{right:23px;top:118px;font-size:16px;font-weight:500;color:#fff}
  .cover .headline{right:23px;top:149px;text-align:right;font-size:21px;line-height:27px;font-weight:700;color:#fff}
  .cover .headline em{font-style:normal;color:var(--orange)}
  .cover .tagline{right:23px;top:211px;font-size:7.5px;color:#fff}

  /* statement */
  .statement .edge{left:0;top:0;width:4.5px;height:259px;background:var(--orange)}
  .statement .glow{left:40px;top:20px;width:320px;height:240px;border-radius:50%;background:radial-gradient(closest-side,rgba(255,226,219,.55),rgba(255,226,219,0))}
  .statement .copy{left:0;right:0;top:88px;text-align:center}
  .statement .kicker{font-size:14px;font-weight:700;color:var(--orange);line-height:18px}
  .statement .lead{font-size:16px;font-weight:700;margin-top:9px;line-height:20px}
  .statement .big{font-size:24.5px;font-weight:800;margin-top:8px;line-height:30px}

  /* contents */
  .toc .title{left:22px;top:78px;font-weight:800;line-height:26px}
  .toc .title span{display:block}
  .toc .t1{font-size:16px}.toc .t2{font-size:20px}
  .toc .intro{left:22px;top:134px;width:112px;font-size:6.4px;line-height:14.6px;color:var(--body)}
  .toc .pill{left:147px;top:0;width:131px;height:259px;border-radius:66px;background:linear-gradient(170deg,var(--slate) 0%,#1c2836 60%,var(--ink) 100%)}
  .toc .list{left:305px;top:43px;list-style:none}
  .toc .list li{font-size:8.8px;line-height:28.7px;color:#2a2d33}
  .toc .list b{font-weight:400;display:inline-block;width:21px}

  /* content slide template */
  .label{left:22px;top:20px;font-size:7px;font-weight:600;color:var(--orange)}
  .heading{left:22px;top:31px;font-size:14px;font-weight:800;white-space:nowrap}
  .rule{left:0;top:57px;width:85px;height:1px;background:var(--orange)}
  .rule::after{content:"";position:absolute;right:-2px;top:-2px;width:5px;height:5px;border-radius:50%;background:var(--orange)}
  .text{left:22px;top:71px;width:184px;font-size:5.6px;line-height:14.4px;color:var(--body);text-align:justify}
  .text p+p{margin-top:14.4px}
  .footer-mark{left:50px;top:211px;width:34px;height:34px;border-radius:50%;background:var(--orange)}
  .footer-bar{left:84px;top:218px;width:376px;height:26.5px;background:var(--orange)}
  .footer-bar .legal{position:absolute;left:11px;top:0;line-height:26.5px;font-size:7.4px;font-weight:500;color:#fff}
  .footer-bar .page{position:absolute;left:268px;top:0;width:79px;height:26.5px;background:var(--ink);color:#fff;font-size:7.4px;font-weight:500;display:flex;align-items:center;justify-content:center}

  .about .ring{left:222px;top:-45px;width:258px;height:258px;border-radius:50%;background:var(--blush)}
  .about .orb{left:226px;top:-41px;width:250px;height:250px;border-radius:50%;background:var(--slate)}

  .classes .frame{left:243px;top:33px;width:190px;height:163px;border-radius:16px;background:var(--ink)}

  .cuisine .back{left:291px;top:20px;width:142px;height:163px;border-radius:16px;background:var(--blush)}
  .cuisine .front{left:229px;top:72px;width:146px;height:132px;border-radius:18px;background:var(--paper);padding:2px}
  .cuisine .front .screen{width:100%;height:100%;border-radius:16px;background:var(--slate);overflow:hidden}

  .market .back{left:291px;top:20px;width:142px;height:170px;border-radius:16px;background:var(--blush)}
  .market .device{left:236px;top:38px;width:80px;height:166px;border-radius:12px;background:#fff;border:3px solid var(--ink)}
  .market .device::before{content:"";position:absolute;left:25px;top:4px;width:24px;height:5px;border-radius:3px;background:var(--ink)}
  .market .device::after{content:"";position:absolute;left:30px;top:70px;width:14px;height:14px;border-radius:50%;background:var(--orange)}

  /* closing */
  .closing{background:var(--orange)}
  .closing .glow{left:40px;top:10px;width:340px;height:250px;border-radius:50%;background:radial-gradient(closest-side,rgba(255,255,255,.12),rgba(255,255,255,0))}
  .closing .thanks{left:0;right:0;top:58px;text-align:center;font-size:32px;font-weight:800;color:#fff;line-height:40px}
  .closing .note{left:55px;right:55px;top:129px;text-align:center;font-size:6.8px;line-height:15px;color:#fff}
  .closing .socials{left:0;right:0;top:171px;display:flex;justify-content:center;gap:7px}
  .closing .socials span{width:21px;height:21px;border-radius:50%;background:#fff}
</style>
</head>
<body>

<!-- Cover -->
<section class="slide cover col-a row-1">
  <div class="abs backdrop"></div>
  <div class="abs drop"></div>
  <div class="shape drop-inner" aria-hidden="true">
    <svg viewBox="0 0 217 214" preserveAspectRatio="none">
      <g fill="#ffe2db" opacity=".9">
        <rect x="30" y="150" width="18" height="64"/>
        <rect x="60" y="128" width="18" height="86"/>
        <rect x="90" y="104" width="18" height="110"/>
        <rect x="120" y="118" width="18" height="96"/>
        <rect x="150" y="80" width="18" height="134"/>
        <rect x="180" y="56" width="18" height="158"/>
      </g>
      <polyline points="10,160 60,110 100,130 140,80 170,95 210,40" fill="none" stroke="#fefefa" stroke-width="2"/>
      <g fill="#fefefa"><circle cx="60" cy="110" r="3.5"/><circle cx="100" cy="130" r="3.5"/><circle cx="140" cy="80" r="3.5"/><circle cx="170" cy="95" r="3.5"/></g>
    </svg>
  </div>
  <div class="abs date">24/06/2024</div>
  <div class="abs brand">Ladle &amp; Line</div>
  <h1 class="abs headline">A New <em>Cooking</em><br>Platform</h1>
  <p class="abs tagline">Ste natus error sit voluptatem accusantium</p>
</section>

<!-- Statement -->
<section class="slide statement col-b row-1">
  <div class="abs glow"></div>
  <div class="abs edge"></div>
  <div class="abs copy">
    <div class="kicker">LADLE LINE</div>
    <div class="lead">DEMAND FOR INTERACTIVE &amp;</div>
    <div class="big">PERSONALIZED EXPERIENCE</div>
  </div>
</section>

<!-- Contents -->
<section class="slide toc col-a row-2">
  <h2 class="abs title"><span class="t1">TABLE OF</span><span class="t2">CONTENTS</span></h2>
  <p class="abs intro">I must explain to you how all this mistaken idea of denouncing pleasure and praising</p>
  <div class="shape pill" aria-hidden="true">
    <svg viewBox="0 0 131 259" preserveAspectRatio="none">
      <g fill="#ff3800">
        <rect x="18" y="170" width="12" height="89"/>
        <rect x="38" y="140" width="12" height="119"/>
        <rect x="58" y="155" width="12" height="104"/>
        <rect x="78" y="110" width="12" height="149"/>
        <rect x="98" y="80" width="12" height="179"/>
      </g>
      <polyline points="0,150 24,135 44,105 64,120 84,75 104,50 131,38" fill="none" stroke="#ffe2db" stroke-width="1.5"/>
    </svg>
  </div>
  <ol class="abs list">
    <li><b>01)</b>Introduction</li>
    <li><b>02)</b>What is Ladle &amp; Line?</li>
    <li><b>03)</b>Virtual Cooking Classes</li>
    <li><b>04)</b>Global Cuisine Exploration</li>
    <li><b>05)</b>Market Opportunity</li>
    <li><b>06)</b>Conclusion</li>
  </ol>
</section>

<!-- Global cuisine -->
<section class="slide cuisine col-b row-2">
  <div class="abs label">LADLE LINE</div>
  <h2 class="abs heading">GLOBAL CUISINE EXPLORATION</h2>
  <div class="abs rule"></div>
  <div class="abs text">
    <p>There is a marked interest in exploring global cuisines through virtual cooking classes. Consumers are eager to learn about and experiment with dishes from different cultures, driven by a desire for new experiences and flavors.</p>
    <p>This trend is facilitated by the accessibility of virtual classes, which can connect chefs and culinary instructors from around the world with interested learners.</p>
  </div>
  <div class="shape back" aria-hidden="true">
    <svg viewBox="0 0 142 163" preserveAspectRatio="none">
      <circle cx="112" cy="40" r="22" fill="#ff3800" opacity=".85"/>
      <circle cx="112" cy="40" r="36" fill="none" stroke="#ff3800" stroke-width="1" opacity=".4"/>
    </svg>
  </div>
  <div class="abs front" aria-hidden="true">
    <div class="screen">
      <svg viewBox="0 0 142 128" preserveAspectRatio="none">
        <g fill="#ffe2db" opacity=".25">
          <rect x="14" y="84" width="10" height="44"/><rect x="34" y="70" width="10" height="58"/>
          <rect x="54" y="78" width="10" height="50"/><rect x="74" y="56" width="10" height="72"/>
          <rect x="94" y="46" width="10" height="82"/><rect x="114" y="30" width="10" height="98"/>
        </g>
        <polyline points="0,96 19,80 39,66 59,74 79,50 99,40 119,24 142,18" fill="none" stroke="#ff3800" stroke-width="2"/>
      </svg>
    </div>
  </div>
  <div class="abs footer-mark"></div>
  <div class="abs footer-bar"><span class="legal">(C) Copyright 2024 | All Rights Reserved</span><span class="page">Page 06 Of 08</span></div>
</section>

<!-- About -->
<section class="slide about col-a row-3">
  <div class="abs label">LADLE LINE</div>
  <h2 class="abs heading">WHAT IS LADLE &amp; LINE?</h2>
  <div class="abs rule"></div>
  <div class="abs text">
    <p>At vero eos et accusamus et iusto odio dignissimos ducimus qui blanditiis praesentium voluptatum deleniti atque corrupti quos dolores et quas molestias excepturi sint occaecati cupiditate non provident, similique sunt in culpa qui officia deserunt mollitia animi, id est laborum et dolorum fuga. Et harum quidem rerum facilis est et expedita distinctio.</p>
    <p>Nam libero tempore, cum soluta nobis est eligendi optio cumque nihil impedit quo minus id quod maxime</p>
  </div>
  <div class="abs ring"></div>
  <div class="shape orb" aria-hidden="true">
    <svg viewBox="0 0 250 250">
      <circle cx="150" cy="150" r="95" fill="none" stroke="#ffe2db" stroke-width="1" opacity=".35"/>
      <circle cx="150" cy="150" r="65" fill="#ff3800"/>
      <circle cx="150" cy="150" r="35" fill="#ffe2db"/>
      <circle cx="72" cy="200" r="16" fill="#010b13" opacity=".5"/>
    </svg>
  </div>
  <div class="abs footer-mark"></div>
  <div class="abs footer-bar"><span class="legal">(C) Copyright 2024 | All Rights Reserved</span><span class="page">Page 03 Of 08</span></div>
</section>

<!-- Market -->
<section class="slide market col-b row-3">
  <div class="abs label">LADLE LINE</div>
  <h2 class="abs heading">MARKET OPPORTUNITY</h2>
  <div class="abs rule"></div>
  <div class="abs text">
    <p>At vero eos et accusamus et iusto odio dignissimos ducimus qui blanditiis praesentium voluptatum deleniti atque corrupti quos dolores et quas molestias excepturi sint occaecati cupiditate non provident, similique sunt in culpa qui officia deserunt mollitia animi, id est laborum et dolorum fuga.</p>
    <p>Et harum quidem rerum facilis est et expedita distinctio. Nam libero tempore, cum soluta nobis est eligendi optio</p>
  </div>
  <div class="shape back" aria-hidden="true">
    <svg viewBox="0 0 142 170" preserveAspectRatio="none">
      <g fill="#2d3e50">
        <rect x="86" y="120" width="12" height="50"/>
        <rect x="104" y="98" width="12" height="72"/>
        <rect x="122" y="72" width="12" height="98"/>
      </g>
      <polyline points="80,110 98,92 116,70 136,44" fill="none" stroke="#ff3800" stroke-width="2"/>
      <circle cx="136" cy="44" r="3.5" fill="#ff3800"/>
    </svg>
  </div>
  <div class="abs device" aria-hidden="true"></div>
  <div class="abs footer-mark"></div>
  <div class="abs footer-bar"><span class="legal">(C) Copyright 2024 | All Rights Reserved</span><span class="page">Page 07 Of 08</span></div>
</section>

<!-- Virtual classes -->
<section class="slide classes col-a row-4">
  <div class="abs label">LADLE LINE</div>
  <h2 class="abs heading">VIRTUAL COOKING CLASSES</h2>
  <div class="abs rule"></div>
  <div class="abs text">
    <p>Consumers seeking alternatives, more choices, easier preference management, or simply a way to avoid crowded spaces are increasingly turning to online culinary education platforms.</p>
    <p>This trend is fueled by the desire to learn new cooking skills, explore different cuisines, and enjoy cooking as a leisure activity or a bonding experience with friends and family, even if remotely</p>
  </div>
  <div class="shape frame" aria-hidden="true">
    <svg viewBox="0 0 190 163" preserveAspectRatio="none">
      <g fill="#2d3e50">
        <rect x="14" y="60" width="8" height="103"/><rect x="168" y="50" width="8" height="113"/>
        <rect x="30" y="90" width="8" height="73"/><rect x="152" y="80" width="8" height="83"/>
      </g>
      <g fill="#ff3800">
        <rect x="62" y="118" width="22" height="45"/>
        <rect x="86" y="90" width="22" height="73"/>
        <rect x="110" y="108" width="22" height="55"/>
      </g>
      <circle cx="97" cy="54" r="22" fill="none" stroke="#ffe2db" stroke-width="3"/>
      <circle cx="97" cy="54" r="8" fill="#ffe2db"/>
    </svg>
  </div>
  <div class="abs footer-mark"></div>
  <div class="abs footer-bar"><span class="legal">(C) Copyright 2024 | All Rights Reserved</span><span class="page">Page 04 Of 08</span></div>
</section>

<!-- Closing -->
<section class="slide closing col-b row-4">
  <div class="abs glow"></div>
  <h2 class="abs thanks">THANK YOU</h2>
  <p class="abs note">At vero eos et accusamus et iusto odio dignissimos ducimus qui blanditiis praesentium voluptatum deleniti atque corrupti quos dolores et quas molestias excepturi sint occaecati</p>
  <div class="abs socials" aria-label="Social channels"><span></span><span></span><span></span></div>
</section>

</body>
</html>
```